Redesign of 15 emails for a Software Company

Hello and welcome to our project. We are in need of a designer to create 15 different emails in HTML that one of our software programs uses. I’ve attached the 15 emails for your review. These emails were created about 4 years ago and are outdated as far as design/ style / font etc is concerned.

FOR THE CONTEST, WE WOULD LIKE YOU TO CREATE AN EMAIL FOR #1 (01 Welcome Email - Buyer and Seller) If you are able to do a second email that would be great so that we can have an idea of what the others will look like. Based on these designs (we will pick the best one) to do all 15 emails.

Must be HTML

DESIGN / FEEL
We are looking to have these emails totally refreshed. We are looking for a much more modern and cleaner feel. More like how Tovel does their emails etc.

COLORS
Colors to be mostly greys and whites (neutral colors).

UNIFORMITY
Although each email will have its own attributes, we would like a common theme for all the emails.

***Please use new Voxlets ... Slatix... equpiment
***Also we included a screenshot of an email template that we found on the internet that we like. We uploaded it to "Look and Feel Sliders" for a frame of reference.

Font styles to use
Sans Serif

Requirements
Must have
• New SLATIX or Computers .. modern font ... neutral colors -- grey.white etc

```html
<!DOCTYPE html>
<html lang="en">
<head>
<meta charset="utf-8">
<title>Create your user account</title>
<link rel="stylesheet" href="https://fonts.googleapis.com/css2?family=Montserrat:wght@400;500;600;700&family=Poppins:wght@400;500;600&family=Roboto:wght@400&display=swap">
<style>
  :root {
    --topbar: #6b8aa0;
    --white: #ffffff;
    --panel: #f1f1f1;
    --mint: #ebf3f2;
    --ink: #2b2b2b;
    --ink-soft: #3c3c3c;
    --avatar-ring: #3a3735;
    --avatar-fill: #8e8e8e;
    --avatar-dark: #4a4a4a;
    --button: #2a2a2a;
  }
  * { margin: 0; padding: 0; box-sizing: border-box; }
  html, body { width: 1200px; height: 3465px; overflow: hidden; background: var(--white); }
  body { font-family: "Poppins", sans-serif; color: var(--ink); }
  .email { position: relative; width: 1200px; height: 3465px; }
  section { position: relative; width: 1200px; }

  .topbar { height: 75px; background: var(--topbar); color: var(--white); font-family: "Roboto", sans-serif; font-size: 21px; text-align: center; line-height: 66px; }

  .masthead { height: 200px; background: var(--white); }
  .brand { position: absolute; left: 165px; top: 60px; font-family: "Montserrat", sans-serif; font-weight: 700; font-size: 46px; color: var(--ink); letter-spacing: 1px; }
  .contact { position: absolute; left: 743px; top: 33px; font-family: "Montserrat", sans-serif; font-size: 20px; line-height: 25px; color: var(--ink-soft); letter-spacing: 1px; }
  .contact .gap { margin-top: 14px; }
  .contact b { font-weight: 700; }

  .intro { height: 1135px; background: var(--panel); text-align: center; }
  .intro h1 { position: absolute; top: 76px; width: 100%; font-family: "Montserrat", sans-serif; font-weight: 600; font-size: 38px; line-height: 44px; color: var(--ink); }
  .hero-device { position: absolute; left: 150px; top: 235px; width: 900px; height: 428px; background: linear-gradient(180deg, #2e2a3c 0%, #5b5470 55%, #332f44 88%, #dcdcdc 100%); }
  .greeting { position: absolute; top: 730px; width: 100%; font-family: "Montserrat", sans-serif; font-weight: 500; font-size: 27px; }
  .intro .body { position: absolute; top: 805px; left: 198px; width: 804px; font-family: "Montserrat", sans-serif; font-size: 20px; line-height: 33px; color: var(--ink-soft); }
  .intro .thanks { position: absolute; top: 972px; width: 100%; font-family: "Montserrat", sans-serif; font-size: 20px; color: var(--ink-soft); }
  .intro .signoff { position: absolute; top: 1034px; width: 100%; font-family: "Montserrat", sans-serif; font-weight: 600; font-size: 24px; letter-spacing: 1px; }

  .divider { height: 12px; background: var(--white); }

  .account { height: 389px; background: var(--mint); text-align: center; }
  .avatar { position: absolute; left: 513px; top: 39px; }
  .account h2 { position: absolute; top: 243px; width: 100%; font-family: "Montserrat", sans-serif; font-weight: 600; font-size: 38px; }
  .account .username { position: absolute; top: 298px; left: 0; width: 100%; font-family: "Montserrat", sans-serif; font-weight: 600; font-size: 26px; letter-spacing: 1px; }
  .account .username span { border-bottom: 2px solid var(--ink); padding-bottom: 2px; }

  .instructions-head { height: 186px; background: var(--panel); text-align: center; }
  .instructions-head h2 { position: absolute; top: 40px; width: 100%; font-family: "Montserrat", sans-serif; font-weight: 600; font-size: 37px; }
  .instructions-head p { position: absolute; top: 106px; width: 100%; font-family: "Montserrat", sans-serif; font-weight: 500; font-size: 27px; letter-spacing: 1px; color: var(--ink-soft); }

  .workspace-photo { height: 588px; background: linear-gradient(100deg, #b79a86 0%, #a46f5e 30%, #d9cfc8 58%, #eef2f6 100%); }

  .steps { height: 657px; background: var(--panel); }
  .steps ol { position: absolute; left: 189px; top: 60px; width: 720px; list-style: none; font-size: 22px; line-height: 36px; color: var(--ink); }
  .steps li { margin-bottom: 9px; }
  .steps .support { position: absolute; left: 189px; top: 373px; width: 800px; font-size: 22px; line-height: 36px; }
  .steps .support b { font-weight: 600; }
  .cta { position: absolute; left: 189px; top: 512px; width: 477px; height: 89px; border-radius: 45px; background: var(--button); color: var(--white); font-family: "Montserrat", sans-serif; font-weight: 600; font-size: 27px; letter-spacing: 1px; line-height: 89px; text-align: center; text-decoration: none; }

  .footer { height: 212px; background: var(--white); text-align: center; font-size: 19px; color: var(--ink); }
  .footer .copy { position: absolute; top: 67px; width: 100%; }
  .footer .prefs { position: absolute; top: 100px; width: 100%; }
  .footer a { color: var(--ink); font-weight: 600; }
</style>
</head>
<body>
<div class="email">
  <section class="topbar">Don't see this email properly? View in web browser</section>

  <section class="masthead">
    <div class="brand">Northlane</div>
    <div class="contact">
      <p>Lindenweg 24, 4511 KR</p>
      <p>Veldhaven, 204718</p>
      <p class="gap"><b>P:</b> 5550 .2187.4432</p>
      <p><b>E:</b> hello@northlane.example</p>
      <p><b>W:</b>www.northlane.example</p>
    </div>
  </section>

  <section class="intro">
    <h1>Create your user account for<br>Closing Portal Suite</h1>
    <div class="hero-device" role="img" aria-label="Laptop showing a dusky desert wallpaper with the word Hello"></div>
    <p class="greeting">Dear {%BROKERNAME%},</p>
    <p class="body">In preparation for your closing, we are sending you this email so that you can set up your password for Closing Portal Suite. This is important so that we can provide you with updates on the progress of all your closings with {%TITLECOMPANY%}.</p>
    <p class="thanks">Thank you and we look forward to serving you and your clients.</p>
    <p class="signoff">{%TITLECOMPANY%}</p>
  </section>

  <section class="divider"></section>

  <section class="account">
    <svg class="avatar" width="174" height="174" viewBox="0 0 176 176" aria-hidden="true">
      <circle cx="88" cy="88" r="86" fill="var(--avatar-ring)"/>
      <circle cx="88" cy="88" r="74" fill="var(--avatar-fill)"/>
      <circle cx="88" cy="62" r="28" fill="var(--avatar-dark)"/>
      <path d="M36 128 C40 100 60 94 88 94 C116 94 136 100 140 128 C128 146 108 152 88 152 C68 152 48 146 36 128 Z" fill="var(--avatar-dark)"/>
      <rect x="87" y="30" width="2" height="124" fill="#6a6a6a"/>
    </svg>
    <h2>Your Username</h2>
    <p class="username"><span>{%USERNAME%}</span></p>
  </section>

  <section class="divider"></section>

  <section class="instructions-head">
    <h2>Instructions</h2>
    <p>How&nbsp; to set up your user account</p>
  </section>

  <section class="workspace-photo" role="img" aria-label="Person at a desk with a laptop and a cup of coloured pencils"></section>

  <section class="steps">
    <ol>
      <li>1.) Click on the setup password button below</li>
      <li>2.) Choose your method of authentication (SMS text or automated phone call) to receive the code</li>
      <li>3.) Once received, enter the code</li>
      <li>4.) Create your password by entering it twice</li>
      <li>5.) Your user account is set up! Now simply put in your username and password to log in</li>
    </ol>
    <p class="support">Thank you and if you have any technical&nbsp; questions or issues, please don't hesitate to email <b>support@closingportal.example</b></p>
    <a class="cta" href="#">SETUP YOUR PASSWORD</a>
  </section>

  <section class="footer">
    <p class="copy">&copy; 2020, Your Company Name</p>
    <p class="prefs">Don't want to receive email. please change your <a href="#">preference</a> or <a href="#">unsubscribe</a> us.</p>
  </section>
</div>
</body>
</html>
```